Needing business card for being Aesthetic nurse
cosmetic nurse injector, medical, cosmetic , aesthetic
Needing business card for being Aesthetic nurse - Medical
Creative Brief
Simple
Corvale Aesthetic Consulting and Training
Tessa K, RN owner, practitioner
4726F Pranton Loop Suite 7 Halvern, MN 55984
corvale@mailtrove.example
I need one....
What I offer: I am looking for cards with charachter, using my logo and web colors of turquoise, silveer and black Consulting individual and small groups Training basic and advanced I also want to use light plastic cards for my business cards
rosewing4 rosewing4
All look really great, I don't like saying owner on anything... TessaKirwood, RN Aesthetic Nurse Individual consulting Maybe try black background?? Thank you again

```html
<!DOCTYPE html>
<html lang="en">
<head>
<meta charset="utf-8">
<title>Corvale Aesthetic Consulting and Training – Business Card</title>
<link rel="stylesheet" href="https://fonts.googleapis.com/css2?family=Open+Sans:wght@400;600&family=Oswald:wght@600&display=swap">
<style>
  :root {
    --page-bg: #e4e7ea;
    --card-fill: rgba(255, 255, 255, 0.78);
    --card-edge: #b8bdc3;
    --turquoise: #17a9a1;
    --silver: #a9afb6;
    --ink: #141414;
    --ink-soft: #3d3f42;
    --icon-glyph: #ffffff;
  }
  * { box-sizing: border-box; margin: 0; padding: 0; }
  html, body {
    width: 1200px; height: 926px; overflow: hidden;
    background: var(--page-bg);
    font-family: "Open Sans", Arial, sans-serif;
    color: var(--ink);
  }
  .canvas { position: relative; width: 1200px; height: 926px; }
  .card {
    position: absolute; left: 240px;
    width: 720px; height: 411px;
    background: var(--card-fill);
    border: 2px solid var(--silver);
    border-radius: 14px;
    box-shadow: 0 8px 24px rgba(40, 50, 60, 0.12);
    overflow: hidden;
  }
  .card--back { top: 40px; }
  .card--front { top: 475px; }

  .brand {
    position: absolute;
    display: flex; align-items: center; gap: 10px;
    font-family: "Open Sans", Arial, sans-serif;
    font-weight: 600; color: var(--turquoise);
    letter-spacing: 1px; line-height: 1;
  }
  .brand__mark { width: 14px; height: 14px; background: var(--turquoise); }
  .card--back .brand { left: 70px; top: 190px; font-size: 44px; }
  .card--front .brand { right: 60px; top: 56px; font-size: 36px; }

  .offer {
    position: absolute; left: 380px; top: 70px; width: 300px;
    padding-left: 22px;
    border-left: 3px solid var(--silver);
  }
  .offer__title {
    font-family: "Oswald", "Arial Narrow", sans-serif;
    font-weight: 600; font-size: 30px; color: var(--turquoise);
    text-transform: uppercase; line-height: 1.1; margin-bottom: 8px;
  }
  .offer__list { list-style: none; font-size: 24px; line-height: 1.25; color: var(--ink); }

  .identity {
    position: absolute; left: 38px; bottom: 30px;
    writing-mode: vertical-rl; transform: rotate(180deg);
    display: flex; flex-direction: row-reverse; gap: 6px;
  }
  .identity__name {
    font-family: "Oswald", "Arial Narrow", sans-serif;
    font-weight: 600; font-size: 34px; color: var(--turquoise);
    text-transform: uppercase; letter-spacing: 1px;
  }
  .identity__role { font-size: 19px; color: var(--ink-soft); }

  .contacts {
    position: absolute; left: 140px; bottom: 34px;
    list-style: none; font-size: 19px; line-height: 1.55; color: var(--ink);
  }
  .contacts__item { display: flex; align-items: center; gap: 12px; }
  .contacts__icon { width: 20px; height: 20px; flex: none; }
  .contacts__icon .disc { fill: var(--turquoise); }
  .contacts__icon .glyph-fill { fill: var(--icon-glyph); }
  .contacts__icon .glyph-line { fill: none; stroke: var(--icon-glyph); stroke-width: 1.3; }
  .contacts__icon .glyph-hole { fill: var(--turquoise); }
</style>
</head>
<body>
<main class="canvas">
  <section class="card card--back" aria-label="Card back">
    <div class="brand"><span class="brand__mark"></span>corvale</div>
    <div class="offer">
      <h2 class="offer__title">What I offer:</h2>
      <ul class="offer__list">
        <li>Consulting individual and small groups</li>
        <li>Training basic and advanced</li>
      </ul>
    </div>
  </section>

  <section class="card card--front" aria-label="Card front">
    <div class="brand"><span class="brand__mark"></span>corvale</div>
    <div class="identity">
      <span class="identity__name">Tessa K</span>
      <span class="identity__role">RN Aesthetic Nurse</span>
    </div>
    <ul class="contacts">
      <li class="contacts__item">
        <svg class="contacts__icon" viewBox="0 0 20 20" aria-hidden="true"><circle class="disc" cx="10" cy="10" r="10"/><path class="glyph-fill" d="M7 5.5l2 2-1 1.2c.6 1.4 1.6 2.4 3 3l1.2-1 2 2-1.2 1.6C9.5 14 6 10.5 5.6 7.2z"/></svg>
        555-013-2846
      </li>
      <li class="contacts__item">
        <svg class="contacts__icon" viewBox="0 0 20 20" aria-hidden="true"><circle class="disc" cx="10" cy="10" r="10"/><circle class="glyph-line" cx="10" cy="10" r="5"/><path class="glyph-line" d="M5 10h10M10 5c-2.5 3-2.5 7 0 10M10 5c2.5 3 2.5 7 0 10"/></svg>
        www.corvaleconsulting.example
      </li>
      <li class="contacts__item">
        <svg class="contacts__icon" viewBox="0 0 20 20" aria-hidden="true"><circle class="disc" cx="10" cy="10" r="10"/><rect class="glyph-line" x="5" y="6.5" width="10" height="7"/><path class="glyph-line" d="M5 6.5l5 4 5-4"/></svg>
        corvale@mailtrove.example
      </li>
      <li class="contacts__item">
        <svg class="contacts__icon" viewBox="0 0 20 20" aria-hidden="true"><circle class="disc" cx="10" cy="10" r="10"/><path class="glyph-fill" d="M10 15.5s-4-4-4-7a4 4 0 018 0c0 3-4 7-4 7z"/><circle class="glyph-hole" cx="10" cy="8.5" r="1.4"/></svg>
        4726F Pranton Loop Suite 7 Halvern, MN 55984
      </li>
    </ul>
  </section>
</main>
</body>
</html>
```